Kelvoro Global corporate slide deck

We are looking for a custom powerpoint template to use both internally and externally with clients and during trainings/presentations. Our customers/clients often include a lot of government agencies, and we specialize in forensics, biometrics, and identity intelligence.
Requirements:
• Title slide
• Section slide
• Title and content slide
• Every slide branded
• Every slide (other than title) includes slide number (x of y), title, and date
• Modern-looking but conservative
• Visually appealing
• Source Sans Pro font
• Call out boxes

The circle in our logo does not signify or mean anything in any way, but we also don't mind it being used as a design element. We also like pulling the blue to red gradient.
Ideally we do not want to use any images of people, but iconography is likely okay.

```html
<!DOCTYPE html>
<html lang="en">
<head>
<meta charset="utf-8">
<title>Our Strengths – Kelvoro Global</title>
<link rel="stylesheet" href="https://fonts.googleapis.com/css2?family=Oswald:wght@300&family=Source+Sans+3:wght@400;700&display=swap">
<style>
  :root {
    --crimson: #a50f45;
    --white: #ffffff;
    --page: #ffffff;
    --footer-text: #6f6f6f;
    --brand-navy: #2a2f7a;
    --brand-purple: #6a2a8c;
    --visual-dark: #2f3438;
    --visual-mid: #5a6268;
    --visual-blue: #2f6fc4;
  }
  * { box-sizing: border-box; margin: 0; padding: 0; }
  html, body { width: 1200px; height: 675px; overflow: hidden; background: var(--page); }
  .slide { position: relative; width: 1200px; height: 675px; background: var(--page); font-family: "Source Sans 3", "Source Sans Pro", sans-serif; color: var(--white); }

  .panel { position: absolute; background: var(--crimson); }

  .intro { left: 54px; top: 50px; width: 723px; height: 186px; text-align: center; padding: 26px 26px 0; }
  .intro-title { font-family: "Oswald", sans-serif; font-weight: 300; font-size: 42px; line-height: 1; text-transform: uppercase; letter-spacing: -0.5px; margin-bottom: 10px; }
  .intro-text { font-weight: 700; font-size: 13.5px; line-height: 1.32; }

  .strength { top: 253px; width: 168px; height: 168px; }
  .strength svg { position: absolute; left: 56px; top: 34px; width: 56px; height: 56px; }
  .strength-label { position: absolute; left: 0; right: 0; top: 108px; text-align: center; font-weight: 700; font-size: 13.5px; text-transform: uppercase; }
  .strength-1 { left: 54px; }
  .strength-2 { left: 239px; }
  .strength-3 { left: 424px; }
  .strength-4 { left: 609px; }

  .stats { left: 54px; top: 439px; width: 723px; height: 186px; }
  .stat { position: absolute; left: 0; width: 290px; top: 58px; text-align: center; }
  .stat-number { font-family: "Oswald", sans-serif; font-weight: 300; font-size: 54px; line-height: 1; letter-spacing: -1.5px; }
  .stat-caption { font-weight: 700; font-size: 13.5px; text-transform: uppercase; margin-top: 2px; }
  .stats-text { position: absolute; left: 288px; width: 426px; top: 48px; font-weight: 700; font-size: 13.5px; line-height: 1.32; text-align: center; }

  .visual { position: absolute; left: 795px; top: 50px; width: 351px; height: 575px;
    background: radial-gradient(circle at 88% 52%, var(--visual-blue) 0%, #274a7a 16%, var(--visual-mid) 40%, var(--visual-dark) 100%); }

  .footer { position: absolute; left: 54px; right: 54px; top: 644px; height: 14px; font-size: 10px; color: var(--footer-text); }
  .footer-date { position: absolute; left: 0; top: 0; }
  .footer-title { position: absolute; left: 0; right: 0; top: 0; text-align: center; text-transform: uppercase; }
  .brand { position: absolute; right: 58px; top: -6px; display: flex; align-items: center; gap: 5px; font-weight: 700; font-size: 12px; color: var(--brand-navy); }
  .brand-dot { width: 18px; height: 18px; border-radius: 50%; border: 2px solid var(--brand-purple); }
  .page-number { position: absolute; right: 0; top: 0; }
</style>
</head>
<body>
<main class="slide">
  <section class="panel intro">
    <h1 class="intro-title">Our Strengths</h1>
    <p class="intro-text">Lorem ipsum dolor sit amet, consectetuer adipiscing elit. Aenean commodo ligula eget dolor. Aenean massa. Cum sociis natoque penatibus et magnis dis parturient montes, nascetur ridiculus mus. Donec quam felis, ultricies nec, pellentesque eu, pretium quis, sem. Nulla consequat massa quis enim. Donec pede justo, fringilla vel, aliquet nec, vulputate eget, arcu.</p>
  </section>

  <div class="panel strength strength-1">
    <svg viewBox="0 0 56 56" fill="none" stroke="#fff" stroke-width="3" stroke-linecap="round">
      <circle cx="32" cy="32" r="16"/><path d="M32 32V23M28 10h8M32 10v6M44 18l3-3"/><path d="M4 26h10M7 33h8M4 40h10"/>
    </svg>
    <span class="strength-label">Fast Delivery</span>
  </div>
  <div class="panel strength strength-2">
    <svg viewBox="0 0 56 56" fill="none" stroke="#fff" stroke-width="3" stroke-linecap="round">
      <circle cx="30" cy="20" r="14"/><path d="M26 32v18M30 20l14 18M6 36h14"/><circle cx="26" cy="20" r="4"/>
    </svg>
    <span class="strength-label">Search Approach</span>
  </div>
  <div class="panel strength strength-3">
    <svg viewBox="0 0 56 56" fill="none" stroke="#fff" stroke-width="3" stroke-linecap="round">
      <circle cx="28" cy="36" r="16"/><path d="M12 36h32M28 20v32M18 24c6 6 14 6 20 0M18 48c6-6 14-6 20 0"/><circle cx="18" cy="8" r="4" fill="#fff"/><circle cx="38" cy="8" r="4" fill="#fff"/>
    </svg>
    <span class="strength-label">Global Network</span>
  </div>
  <div class="panel strength strength-4">
    <svg viewBox="0 0 56 56" fill="none" stroke="#fff" stroke-width="3" stroke-linecap="round">
      <circle cx="24" cy="32" r="16"/><circle cx="24" cy="32" r="6"/><path d="M24 32L48 8M40 8h8v8M24 10v6M24 48v6M2 32h6M40 32h6"/>
    </svg>
    <span class="strength-label">Target Driven</span>
  </div>

  <section class="panel stats">
    <div class="stat">
      <div class="stat-number">12.418.126</div>
      <div class="stat-caption">Visitors since 2015</div>
    </div>
    <p class="stats-text">Lorem ipsum dolor sit amet, consectetuer adipiscing elit. Aenean commodo ligula eget dolor. Aenean massa. Cum sociis natoque penatibus et magnis dis parturient montes, nascetur ridiculus mus. Donec quam felis, ultricies nec, pellentesque eu, pretium quis, sem. Nulla consequat massa quis enim.</p>
  </section>

  <div class="visual" role="img" aria-label="Close-up biometric eye scan with a blue digital targeting overlay"></div>

  <footer class="footer">
    <span class="footer-date">26.06.24</span>
    <span class="footer-title">Date | Presentation Title</span>
    <span class="brand"><span class="brand-dot"></span>Kelvoro Global</span>
    <span class="page-number">14 of 24</span>
  </footer>
</main>
</body>
</html>
```